Design business card for Bright Harbour Coaching!

I am a personal development coach (like a life coach) and corporate trainer and need a professionally designed double sided business card.

It needs to contain the business logo (I'm happy for the designer to choose the layout of the logo as I am still working out the best option myself) and the following information:

Corinne Vashti
Personal Development Coach and Trainer

+61 (0)452 918 637 (written that way)
corinne@bright-harbour.example

www.bright-harbour.example

```html
<!DOCTYPE html>
<html lang="en">
<head>
<meta charset="utf-8">
<title>Bright Harbour Coaching – Business Card</title>
<link href="https://fonts.googleapis.com/css2?family=Cinzel:wght@400&family=Open+Sans:wght@400;600;700&display=swap" rel="stylesheet">
<style>
  :root {
    --teal: #0a8a96;
    --black: #0b0b0c;
    --silver: #cfd1d3;
    --white: #ffffff;
    --light-grey: #d8d8d8;
    --backdrop: #e6e6e4;
  }
  * { margin: 0; padding: 0; box-sizing: border-box; }
  html, body {
    width: 1200px; height: 900px; overflow: hidden;
    background: var(--backdrop);
    font-family: "Open Sans", Arial, sans-serif;
  }
  .canvas { position: relative; width: 1200px; height: 900px; }
  .card {
    position: absolute; left: 300px; width: 600px; height: 343px;
    border-radius: 4px; overflow: hidden;
    box-shadow: 0 6px 18px rgba(0,0,0,0.18);
    background: var(--teal);
  }
  .card--back { top: 64px; }
  .card--front { top: 471px; }

  .brand {
    position: absolute; display: flex; align-items: center; gap: 16px;
    white-space: nowrap;
  }
  .brand__dot { flex: 0 0 auto; width: 40px; height: 40px; border-radius: 50%; }
  .brand__name {
    font-family: "Cinzel", Georgia, serif; font-weight: 400;
    font-size: 26px; letter-spacing: 0.5px; line-height: 1;
  }
  .card--back .brand { left: 50%; top: 120px; transform: translateX(-50%); }
  .card--back .brand__dot { background: var(--white); }
  .card--back .brand__name { color: var(--white); }
  .card--back .website {
    position: absolute; left: 0; right: 0; top: 205px; text-align: center;
    color: var(--white); font-weight: 700; font-size: 13px;
  }

  .front-art { position: absolute; left: 0; top: 0; display: block; }
  .card--front .brand { left: 44px; top: 40px; }
  .card--front .brand__dot { background: var(--teal); }
  .card--front .brand__name { color: var(--light-grey); }

  .person { position: absolute; left: 40px; top: 178px; color: var(--white); }
  .person__name { font-weight: 700; font-size: 20px; line-height: 1.2; }
  .person__title { font-size: 15px; line-height: 1.35; }

  .contact {
    position: absolute; right: 32px; bottom: 36px; list-style: none;
    color: var(--white); font-size: 16px; text-align: right;
  }
  .contact__item {
    display: flex; justify-content: flex-end; align-items: center; gap: 12px;
    line-height: 1.55;
  }
  .contact__icon { width: 14px; height: 14px; fill: none; stroke: var(--white); stroke-width: 1.6; }
</style>
</head>
<body>
<main class="canvas">

  <section class="card card--back" aria-label="Card back">
    <div class="brand">
      <span class="brand__dot"></span>
      <span class="brand__name">BRIGHT HARBOUR COACHING</span>
    </div>
    <p class="website">www.bright-harbour.example</p>
  </section>

  <section class="card card--front" aria-label="Card front">
    <svg class="front-art" viewBox="0 0 600 343" width="600" height="343" aria-hidden="true">
      <path fill="var(--black)" d="M-2 -2 H602 V120 L600 120 C420 175 200 150 0 55 L-2 55 Z"/>
      <path fill="var(--silver)" d="M-2 55 L0 55 C200 150 420 175 600 120 L602 120 V133 L600 132 C420 190 200 170 0 85 L-2 85 Z"/>
    </svg>
    <div class="brand">
      <span class="brand__dot"></span>
      <span class="brand__name">BRIGHT HARBOUR COACHING</span>
    </div>
    <div class="person">
      <p class="person__name">Corinne Vashti</p>
      <p class="person__title">Personal Development Coach and Trainer</p>
    </div>
    <ul class="contact">
      <li class="contact__item">+61 (0)452 918 637
        <svg class="contact__icon" viewBox="0 0 16 16"><path d="M3 2 L6 2 L7 5 L5 6.5 C6 9 7 10 9.5 11 L11 9 L14 10 L14 13 C8 14 2 8 3 2 Z"/></svg>
      </li>
      <li class="contact__item">corinne@bright-harbour.example
        <svg class="contact__icon" viewBox="0 0 16 16"><rect x="1.5" y="3.5" width="13" height="9"/><path d="M1.5 3.5 L8 9 L14.5 3.5"/></svg>
      </li>
      <li class="contact__item">www.bright-harbour.example
        <svg class="contact__icon" viewBox="0 0 16 16"><path d="M7 9 L9 7"/><path d="M6 7 L3.5 9.5 A2.1 2.1 0 0 0 6.5 12.5 L9 10"/><path d="M10 9 L12.5 6.5 A2.1 2.1 0 0 0 9.5 3.5 L7 6"/></svg>
      </li>
    </ul>
  </section>

</main>
</body>
</html>
```